Bright Harbour - website for leadership service

I would like help to use a Squarespace template for a simple website.
We already have a logo which will influence the colour choice and tone.
Clean lines for executive audience. it is an exclusive service. I have all the content ready to go.
Would like some images included.

I will upload the content soon.

Does NOT need SEO as it will be direct mailed. Also does NOT need to consider having any payment pages or enquiry form.
Thanks

Target Market(s)

Women executives - senior leaders. Stylish, serious and capable.

Coding

Coded - Design and coding required

Number of Pages Required

3 page

Colors
3176b5
fee18a

Requirements
Must have
• Sqaurespace template. And scrolling down page format.

To suit style of the blue and gold logo.
Nice to have
• Simple, Stylish and exclusive feel. Inspiring but not "New Age"
Should not have
• Too many colours.

No

```html
<!DOCTYPE html>
<html lang="en">
<head>
<meta charset="utf-8">
<title>Bright Harbour – Leadership Coaching</title>
<link href="https://fonts.googleapis.com/css2?family=Cinzel:wght@400;600&family=Montserrat:wght@400;500&family=Playfair+Display:wght@400;700&display=swap" rel="stylesheet">
<style>
:root{
  --navy:#1a2640;
  --navy-deep:#141d33;
  --gold:#c9a857;
  --gold-soft:#d6bb6d;
  --band-gold:#bd9a55;
  --ink:#2b3348;
  --text:#3d4354;
  --white:#ffffff;
  --ghost:#5b6579;
}
*{box-sizing:border-box;margin:0;padding:0}
html,body{width:1200px;height:3141px;overflow:hidden}
body{position:relative;background:var(--white);font-family:"Montserrat",sans-serif;color:var(--text)}
.abs{position:absolute}
.serif-caps{font-family:"Cinzel",serif}
.btn{position:absolute;background:linear-gradient(180deg,#d4b769,#b8974c);color:var(--white);font-family:"Cinzel",serif;font-size:14px;display:flex;align-items:center;justify-content:center;letter-spacing:.3px}
.rule{position:absolute;height:2px;background:var(--gold)}
.rule::after{content:"";position:absolute;right:-3px;top:-2px;width:6px;height:6px;border-radius:50%;background:var(--gold)}
.photo{position:absolute}

/* hero */
.hero{position:absolute;left:0;top:0;width:1200px;height:510px;background:radial-gradient(ellipse at 60% 20%,#5a5560 0%,#34303a 45%,#1c1a22 100%)}
.logo-name{font-family:"Cinzel",serif;font-size:22px;color:var(--white);letter-spacing:1px}
.logo-dot{width:14px;height:14px;border-radius:50%;background:var(--gold);display:inline-block;margin-right:10px;vertical-align:middle}
.nav a{position:absolute;top:70px;font-family:"Cinzel",serif;font-size:14px;color:var(--white);text-decoration:none}
.hero-title{left:95px;top:318px;width:820px;font-family:"Playfair Display",serif;font-size:45px;line-height:53px;color:var(--white)}

/* intro */
.intro-lead{left:95px;top:560px;width:500px;font-family:"Cinzel",serif;font-size:17px;line-height:27px;color:var(--ink)}
.intro-div{left:615px;top:548px;width:1px;height:142px;background:#c9ccd3}
.intro-side{left:654px;top:570px;width:455px;font-size:14.5px;line-height:21px;color:var(--text)}

/* navy feature sections */
.band-navy{position:absolute;left:0;width:1200px;background:var(--navy)}
.feat-title{font-family:"Cinzel",serif;font-size:29px;line-height:32px;color:var(--gold);letter-spacing:.5px}
.feat-body{font-size:13.5px;line-height:21px;color:var(--white)}
.ghost{font-family:"Cinzel",serif;font-size:50px;color:var(--ghost);letter-spacing:2px}
.dark-title{font-family:"Cinzel",serif;font-size:27px;line-height:33px;color:var(--ink);letter-spacing:.5px}
.dark-body{font-size:13.5px;line-height:21px;color:var(--text)}

/* quote */
.quote{left:135px;top:2282px;width:850px;font-family:"Playfair Display",serif;font-size:22px;line-height:32px;color:var(--ink)}
.quote-name{left:135px;top:2362px;font-family:"Cinzel",serif;font-size:16px;color:var(--ink)}
.quote-mark{left:945px;top:2320px;font-family:"Playfair Display",serif;font-weight:700;font-size:120px;line-height:1;color:var(--gold)}

/* testimonial */
.testi-band{left:0;top:2463px;width:1200px;height:80px;background:var(--band-gold);text-align:center;font-family:"Playfair Display",serif;font-weight:700;font-size:54px;line-height:80px;color:var(--white)}
.testi-bg{left:0;top:2543px;width:1200px;height:287px;background:linear-gradient(180deg,#1b2741,#141e35)}
.testi-name{left:0;top:2610px;width:1200px;text-align:center;font-family:"Cinzel",serif;font-size:22px;color:var(--gold)}
.testi-role{left:0;top:2640px;width:1200px;text-align:center;font-family:"Cinzel",serif;font-size:12px;color:var(--gold)}
.testi-text{left:185px;top:2670px;width:830px;text-align:center;font-size:14px;line-height:26.5px;font-weight:500;color:var(--white)}

/* footer */
.foot-div{position:absolute;top:2875px;width:1px;height:135px;background:#d7d9de}
.foot-head{font-family:"Cinzel",serif;font-size:19px;color:var(--ink)}
.foot-line{position:absolute;height:2px;width:62px;background:var(--gold)}
.foot-list{list-style:none;font-size:13.5px;line-height:26.5px;color:var(--ink);font-weight:500}
.foot-list li{display:flex;align-items:center}
.foot-list svg{margin-right:9px;flex:none}
.social{position:absolute;top:2938px;width:27px;height:27px;border-radius:50%;background:var(--gold)}
.copyright{left:0;top:3106px;width:1200px;text-align:center;font-family:"Cinzel",serif;font-size:12.5px;color:var(--ink)}
</style>
</head>
<body>

<header class="hero" role="img" aria-label="Photo of a large audience seated in a conference hall, darkened"></header>
<div class="abs" style="left:95px;top:60px">
  <span class="logo-dot"></span><span class="logo-name">Bright Harbour</span>
</div>
<nav class="nav">
  <a style="left:677px" href="#">Home</a>
  <a style="left:760px" href="#">About Us</a>
  <a style="left:869px" href="#">Resources</a>
</nav>
<div class="btn" style="left:985px;top:57px;width:120px;height:39px">Contact Us</div>
<h1 class="abs hero-title">Women leadership is a premier leadership coaching service !</h1>

<section>
  <p class="abs intro-lead">We entirely focused on supporting women in executive roles to lead commercially successful businesses in ways that align with their core values and principles.</p>
  <div class="abs intro-div"></div>
  <p class="abs intro-side">A new era of values-driven business has begun, led by women like you: capable, proven leaders who are challenging the status quo and redefining the meaning of business success.</p>
</section>

<section class="band-navy" style="top:733px;height:505px"></section>
<div class="photo" style="left:95px;top:808px;width:484px;height:325px;background:linear-gradient(120deg,#2a2226 0%,#7a3a22 45%,#d86a33 70%,#e9c9a4 100%)" role="img" aria-label="Photo of a speaker addressing a conference audience"></div>
<h2 class="abs feat-title" style="left:653px;top:800px">What is Bright Harbour?</h2>
<div class="rule" style="left:653px;top:855px;width:228px"></div>
<div class="abs feat-body" style="left:652px;top:884px;width:450px">
  <p>Women are at the forefront of a global movement of leaders pioneering new business models. BRIGHT HARBOUR will connect you to this movement and get you excited about business leadership again.</p>
  <p>What made business successful in the past is not working. Long established traditions of politicking, closed door decision making and a constant focus on short-term quick wins and shareholder profit are no longer a guarantee of good business results.</p>
</div>
<div class="btn" style="left:654px;top:1093px;width:119px;height:40px">Read More</div>
<div class="abs ghost" style="left:93px;top:1160px">Women Leadership</div>

<h2 class="abs dark-title" style="left:95px;top:1315px;width:460px">Is it time for me to be a part of Bright Harbour?</h2>
<div class="rule" style="left:95px;top:1407px;width:228px"></div>
<div class="abs dark-body" style="left:96px;top:1436px;width:450px">
  <p>You are already successful, but you may be questioning whether you want to put your hand up for bigger roles. That is entirely understandable with the current business focus on short-term profit and unsustainable demands on people.</p>
  <p style="margin-top:21px">You may feel isolated in busy, demanding roles. You would love to have other women to connect who share the same values.</p>
</div>
<div class="btn" style="left:94px;top:1605px;width:119px;height:39px">Read More</div>
<div class="photo" style="left:621px;top:1318px;width:484px;height:325px;background:linear-gradient(160deg,#f1f1f3 0%,#e3e4e8 60%,#b9b4b0 100%)" role="img" aria-label="Illustrated whiteboard of leadership qualities with a smiling presenter"></div>

<section class="band-navy" style="top:1731px;height:504px"></section>
<div class="photo" style="left:95px;top:1806px;width:484px;height:325px;background:linear-gradient(120deg,#6b4a38 0%,#9a6e55 40%,#d9d2c8 75%,#f3f0ea 100%)" role="img" aria-label="Photo of three businesswomen working together at an office desk"></div>
<h2 class="abs feat-title" style="left:655px;top:1798px;width:450px">How will Bright Harbour help me?</h2>
<div class="rule" style="left:655px;top:1883px;width:228px"></div>
<p class="abs feat-body" style="left:652px;top:1908px;width:450px">No one understands as well as you, the blocks and challenges of working in current business models. BRIGHT HARBOUR will strengthen your leadership with new thinking, new models and the ability to tap into your own deep wisdom.</p>
<p class="abs feat-body" style="left:652px;top:2013px;width:450px;color:var(--gold)">&gt; Navigate current business challenges without compromising your values.</p>
<div class="btn" style="left:652px;top:2092px;width:119px;height:39px">Read More</div>
<div class="abs ghost" style="left:96px;top:2158px">How it Works</div>

<blockquote class="abs quote">“Bright Harbour catalyses our best women leaders, getting them to the forefront of this exciting new wave of business approaches and success”</blockquote>
<div class="abs quote-name">Maren Ellis</div>
<div class="abs quote-mark">”</div>

<h2 class="abs testi-band">Testimonial</h2>
<div class="abs testi-bg"></div>
<div class="abs testi-name">Celia Marsh,</div>
<div class="abs testi-role">CEO at Alder Row Foundation</div>
<p class="abs testi-text">I have had the pleasure of spending the last year working with Maren. Her measured guidance has been a pillar for my success this year. She helped me to find my voice and gave me the confidence to speak up where needed. Maren has helped me to prioritise my time to become more of a leader and less of an administrator. I feel so much more confident in my role with a clear vision into the future.</p>
<svg class="abs" style="left:115px;top:2696px" width="20" height="32" viewBox="0 0 20 32"><path d="M17 2 L3 16 L17 30" fill="none" stroke="#c9a857" stroke-width="3"/></svg>
<svg class="abs" style="left:1065px;top:2696px" width="20" height="32" viewBox="0 0 20 32"><path d="M3 2 L17 16 L3 30" fill="none" stroke="#c9a857" stroke-width="3"/></svg>

<footer>
  <div class="abs" style="left:95px;top:2918px">
    <span class="logo-dot"></span><span class="logo-name" style="color:var(--ink);font-size:20px">Bright Harbour</span>
  </div>
  <div class="foot-div" style="left:353px"></div>
  <div class="foot-div" style="left:590px"></div>
  <div class="foot-div" style="left:925px"></div>

  <h3 class="abs foot-head" style="left:411px;top:2877px">Quick Links</h3>
  <div class="foot-line" style="left:411px;top:2910px"></div>
  <ul class="abs foot-list" style="left:411px;top:2925px">
    <li>Home</li><li>About Us</li><li>Illegal Parking</li><li>Contact Us</li>
  </ul>

  <h3 class="abs foot-head" style="left:671px;top:2877px">Contact</h3>
  <div class="foot-line" style="left:671px;top:2910px"></div>
  <ul class="abs foot-list" style="left:671px;top:2925px">
    <li><svg width="12" height="12" viewBox="0 0 12 12"><path d="M2 1 L4.5 1 L5.5 4 L4 5 Q5 7.5 7 8 L8 6.5 L11 7.5 L11 10 Q6 11.5 2 6 Q0.8 3 2 1Z" fill="#c9a857"/></svg>0161-5550142</li>
    <li><svg width="12" height="12" viewBox="0 0 12 12"><rect x="1" y="3" width="10" height="7" fill="#c9a857"/><path d="M1 3 L6 7 L11 3" fill="none" stroke="#fff" stroke-width="1"/></svg>hello@brightharbour.example</li>
    <li><svg width="12" height="12" viewBox="0 0 12 12"><path d="M6 11 Q1.5 6 1.5 4.5 A4.5 4.5 0 0 1 10.5 4.5 Q10.5 6 6 11Z" fill="#c9a857"/><circle cx="6" cy="4.5" r="1.6" fill="#fff"/></svg>48 Quay Lane,</li>
    <li style="padding-left:21px">Harbour City</li>
  </ul>

  <h3 class="abs foot-head" style="left:965px;top:2877px">Follow Us</h3>
  <div class="foot-line" style="left:965px;top:2910px"></div>
  <span class="social" style="left:965px"></span>
  <span class="social" style="left:1000px"></span>
  <span class="social" style="left:1035px"></span>
  <span class="social" style="left:1070px"></span>

  <p class="abs copyright">Copyright © brightharbour 2020. All rights reserved.</p>
</footer>

</body>
</html>
```